Wine Label - Design required by La Brisuela

2 Independent chilean winemakers here!
La Brisuela (means door slam or slam), that is the brand for our wines (2 wines at the moment), low scale production.
We would like to have front label for our wine out of the mainstream typical french classic style. Some words to describe it: youthful yet vintage/ Tobiah Vance/ pellman/ comic/ old western. Something i would wear on a t-shirt.
The text that is has to be on the label:
- La Brisuela (the brand)
-Field Blend (the type of one of the wines we have)
- 2018
- Wine of Chile.
It goes on sloping shoulder bottle, Burgundy model.
It is meant to cover a space of 3 1/4 h x 4 1/2 w inches . (or 8,5 cm height x 11cm width).
We like colours so...be creative!
I have attached the "La Brisuela" logo. We can changed it of course.
Thanks !

Target Market(s)

young drinkers (legally allowed to drink!)

Font styles to use
Other font styles liked:
• stencil

Colors

Designer to choose colors to be used in the design.

Requirements
Should not have
• Obvious wine things like glasses of wine, vines, grapes etc.

```html
<!DOCTYPE html>
<html lang="en">
<head>
<meta charset="utf-8">
<title>La Brisuela — Field Blend Label</title>
<link rel="stylesheet" href="https://fonts.googleapis.com/css2?family=Cinzel:wght@500&family=Oswald:wght@300&family=Sancreek&display=swap">
<style>
  :root {
    --stage: #1c1c1c;
    --label-red: #8e0a12;
    --teal: #4b9196;
    --teal-dark: #3b7c82;
    --ink: #0f1414;
    --cream: #efe8d6;
    --title-red: #c8202c;
    --ornament-red: #c8343c;
  }
  html, body {
    margin: 0;
    padding: 0;
    width: 1200px;
    height: 792px;
    overflow: hidden;
    background: var(--stage);
  }
  .label {
    position: absolute;
    left: 110px;
    top: 18px;
    width: 980px;
    height: 756px;
    display: block;
  }
  .brand-small, .brand-name { font-family: "Sancreek", serif; fill: var(--title-red); }
  .wine-type { font-family: "Cinzel", serif; font-weight: 500; fill: var(--ink); }
  .info-text { font-family: "Oswald", sans-serif; font-weight: 300; fill: var(--cream); }
</style>
</head>
<body>
<svg class="label" viewBox="0 0 656 506" xmlns="http://www.w3.org/2000/svg">
  <defs>
    <clipPath id="octagon-clip">
      <polygon points="190,0 466,0 656,193 656,313 466,506 190,506 0,313 0,193"/>
    </clipPath>
    <radialGradient id="filigree-tone" cx="50%" cy="55%" r="50%">
      <stop offset="0" stop-color="#d64a50"/>
      <stop offset="0.8" stop-color="#c8343c"/>
      <stop offset="1" stop-color="#c8343c" stop-opacity="0"/>
    </radialGradient>
    <pattern id="star-row" width="12" height="12" patternUnits="userSpaceOnUse">
      <polygon points="6,1.5 7.3,4.7 10.5,5 8,7.1 8.8,10.3 6,8.5 3.2,10.3 4,7.1 1.5,5 4.7,4.7" fill="var(--cream)"/>
    </pattern>
    <pattern id="dot-column" width="10" height="12" patternUnits="userSpaceOnUse">
      <rect x="3" y="4" width="4" height="4" fill="var(--cream)"/>
    </pattern>
    <pattern id="diamond-column" width="12" height="16" patternUnits="userSpaceOnUse">
      <polygon points="6,3 10,8 6,13 2,8" fill="var(--cream)"/>
    </pattern>
  </defs>

  <!-- label ground -->
  <rect class="label-ground" width="656" height="506" fill="var(--label-red)"/>

  <!-- teal octagon with striped bands -->
  <g class="octagon" clip-path="url(#octagon-clip)">
    <rect width="656" height="506" fill="var(--teal)"/>
    <g class="stripes" stroke="var(--ink)" stroke-width="1.2">
      <line x1="0" y1="7" x2="656" y2="7"/>
      <line x1="0" y1="15" x2="656" y2="15"/>
      <line x1="0" y1="23" x2="656" y2="23"/>
      <line x1="0" y1="31" x2="656" y2="31"/>
      <line x1="0" y1="39" x2="656" y2="39"/>
      <line x1="0" y1="467" x2="656" y2="467"/>
      <line x1="0" y1="475" x2="656" y2="475"/>
      <line x1="0" y1="483" x2="656" y2="483"/>
      <line x1="0" y1="491" x2="656" y2="491"/>
      <line x1="0" y1="499" x2="656" y2="499"/>
    </g>
  </g>
  <polygon class="octagon-edge" points="190,0 466,0 656,193 656,313 466,506 190,506 0,313 0,193" fill="none" stroke="var(--ink)" stroke-width="1.5"/>

  <!-- outer frame -->
  <rect class="outer-frame" x="38" y="50" width="580" height="410" fill="var(--teal)" stroke="var(--ink)" stroke-width="2"/>
  <rect class="outer-frame-inner" x="55" y="65" width="546" height="380" fill="none" stroke="var(--ink)" stroke-width="1.2"/>

  <!-- star rows and dotted columns -->
  <g class="frame-trim">
    <rect x="60" y="52" width="84" height="12" fill="url(#star-row)"/>
    <rect x="512" y="52" width="84" height="12" fill="url(#star-row)"/>
    <rect x="60" y="446" width="84" height="12" fill="url(#star-row)"/>
    <rect x="512" y="446" width="84" height="12" fill="url(#star-row)"/>
    <rect x="41" y="70" width="10" height="372" fill="url(#dot-column)"/>
    <rect x="605" y="70" width="10" height="372" fill="url(#dot-column)"/>
    <rect x="69" y="140" width="12" height="224" fill="url(#diamond-column)"/>
    <rect x="544" y="140" width="12" height="224" fill="url(#diamond-column)"/>
  </g>

  <!-- frame corner blocks -->
  <g class="corner-blocks" fill="var(--teal-dark)" stroke="var(--ink)" stroke-width="1.5">
    <rect x="25" y="37" width="25" height="25"/>
    <rect x="606" y="37" width="25" height="25"/>
    <rect x="25" y="448" width="25" height="25"/>
    <rect x="606" y="448" width="25" height="25"/>
  </g>

  <!-- corner ornaments -->
  <g class="corner-ornaments" fill="var(--ink)">
    <polygon role="img" aria-label="Black and white scroll ornament, top left corner" points="58,68 128,68 58,138"/>
    <polygon role="img" aria-label="Black and white scroll ornament, top right corner" points="598,68 528,68 598,138"/>
    <polygon role="img" aria-label="Black and white scroll ornament, bottom left corner" points="58,442 128,442 58,372"/>
    <polygon role="img" aria-label="Black and white scroll ornament, bottom right corner" points="598,442 528,442 598,372"/>
  </g>

  <!-- centre panel -->
  <rect class="centre-panel" x="95" y="83" width="454" height="290" fill="var(--teal)" stroke="var(--ink)" stroke-width="1.5"/>

  <!-- red filigree area -->
  <ellipse class="filigree" role="img" aria-label="Red baroque filigree scrollwork surrounding the medallion, with small black flowers at top and bottom" cx="322" cy="200" rx="210" ry="165" fill="url(#filigree-tone)"/>

  <!-- cream medallion -->
  <ellipse class="medallion" cx="322" cy="180" rx="168" ry="112" fill="var(--cream)"/>

  <!-- brand name -->
  <text class="brand-small" x="322" y="120" text-anchor="middle" font-size="24">LA</text>
  <text class="brand-name" x="322" y="208" text-anchor="middle" font-size="104" textLength="316" lengthAdjust="spacingAndGlyphs">BRISUELA</text>
  <g class="name-rule" fill="var(--ink)">
    <rect x="222" y="218" width="200" height="1.2"/>
    <polygon points="322,214 327,218.6 322,223 317,218.6"/>
  </g>

  <!-- wine type -->
  <text class="wine-type" x="322" y="260" text-anchor="middle" font-size="25" textLength="158" lengthAdjust="spacingAndGlyphs">FIELD BLEND</text>

  <!-- info band -->
  <g class="info-band">
    <polygon points="100,375 558,375 520,454 140,454" fill="var(--ink)"/>
    <line x1="120" y1="414.5" x2="540" y2="414.5" stroke="var(--cream)" stroke-width="1"/>
    <line x1="280" y1="378" x2="280" y2="412" stroke="var(--cream)" stroke-width="1"/>
    <line x1="338" y1="417" x2="338" y2="451" stroke="var(--cream)" stroke-width="1"/>
    <text class="info-text" x="195" y="408" text-anchor="middle" font-size="36" textLength="60" lengthAdjust="spacingAndGlyphs">2018</text>
    <text class="info-text" x="403" y="406" text-anchor="middle" font-size="32" textLength="157" lengthAdjust="spacingAndGlyphs">WINE OF CHILE</text>
    <text class="info-text" x="247" y="446" text-anchor="middle" font-size="26" textLength="121" lengthAdjust="spacingAndGlyphs">14% ALC. VOL</text>
    <text class="info-text" x="415" y="446" text-anchor="middle" font-size="26" textLength="65" lengthAdjust="spacingAndGlyphs">750ML</text>
  </g>
</svg>
</body>
</html>
```